Recruiting agency looking for a newsletter design

We need to design a newsletter that will be sent by e-mail to our clients database. This communication announces a new milestone for our company.

We need it to convey high professionalism, elegance ad luxury. It needs to catch the reader’s attention.

The background needs to be light shiny silver, not flat gray, not dark silver. Some effects can give dimension to the content. We need a very impactful communication.

You will find attached:

- The content that needs to appear on the newsletter
- Pictures “moodboard” that you can take into consideration for the overall “atmosphere” and “emotion” that the design needs to convey. Please DO NOT include any of these images in the newsletter itself. They are just here to help you get the idea of the type of image we want to convey as a company with this communication.
- Company logo
- Please note that I will provide you later on with a URL link to include to the newsletter.

```html
<!DOCTYPE html>
<html lang="en">
<head>
<meta charset="utf-8">
<title>Vantor &amp; Hale — 2021 New Era, New Fees</title>
<link href="https://fonts.googleapis.com/css2?family=Lato:ital,wght@0,400;0,700;1,400&display=swap" rel="stylesheet">
<style>
  :root {
    --silver-top: #c4c4c4;
    --silver-page: #d3d3d3;
    --silver-contact: #c0c0c0;
    --ink: #0c1b26;
    --rule: #5b6a78;
    --sky: #00a5f2;
    --teal: #00bcd8;
    --night: #021822;
    --footer-text: #d6dde2;
    --white: #ffffff;
    --icon: #6e6e6e;
  }
  * { box-sizing: border-box; margin: 0; padding: 0; }
  html, body { width: 1200px; height: 2754px; overflow: hidden; }
  body {
    font-family: "Lato", "Helvetica Neue", Arial, sans-serif;
    color: var(--ink);
    background: var(--silver-page);
  }
  .newsletter { width: 1200px; height: 2754px; position: relative; }

  .masthead {
    height: 158px;
    background: linear-gradient(180deg, #cbcbcb 0%, var(--silver-top) 100%);
    display: flex; align-items: center; justify-content: center; gap: 16px;
  }
  .brand-dot { width: 22px; height: 22px; border-radius: 50%; background: var(--ink); }
  .brand-name { font-size: 34px; font-weight: 400; letter-spacing: 6px; color: var(--ink); }

  .hero {
    height: 438px;
    background: linear-gradient(120deg, #1c2430 0%, #3b3f45 30%, #8a6a4c 55%, #c9a88a 70%, #3a4a66 100%);
  }

  .section-title {
    height: 152px;
    display: flex; align-items: center;
    font-size: 38px; font-weight: 700; letter-spacing: 0.5px;
    white-space: nowrap;
  }
  .section-title::before, .section-title::after {
    content: ""; flex: 1; height: 2px; background: var(--rule);
  }
  .section-title span { padding: 0 32px; }
  .fees-title { height: 152px; }
  .testimonials-title { height: 154px; margin-top: 0; }
  .contact-title { height: 228px; }
  .contact-title.section-title { height: 228px; }

  .fee-grid {
    height: 430px;
    display: flex; justify-content: center; gap: 60px;
    padding-top: 32px;
  }
  .fee-card {
    width: 472px; height: 348px;
    display: flex; flex-direction: column; align-items: center; justify-content: center;
    text-align: center;
  }
  .fee-card--exec { background: var(--sky); }
  .fee-card--other { background: var(--teal); }
  .fee-label { font-size: 40px; line-height: 48px; font-weight: 400; }
  .fee-rate { font-size: 56px; font-weight: 700; margin-top: 6px; }

  .testimonial {
    height: 380px;
    background: linear-gradient(100deg, #2b3850 0%, #1d2a44 40%, #33405a 60%, #141d33 100%);
    color: var(--white);
    text-align: center;
    position: relative;
  }
  .testimonial-photo { position: absolute; inset: 0; }
  .testimonial-copy { position: relative; padding-top: 26px; }
  .testimonial-kicker { font-size: 36px; font-style: italic; line-height: 1; }
  .testimonial-quote {
    font-size: 33px; line-height: 56px; color: #e4e8ee;
    margin: 40px auto 0; width: 1000px;
  }
  .testimonial-author { font-size: 34px; margin-top: 20px; }

  .contact {
    height: 674px;
    background: var(--silver-contact);
    text-align: center;
    padding-top: 46px;
    font-size: 34px;
  }
  .contact-address { line-height: 56px; }
  .contact-email { margin-top: 24px; line-height: 56px; }
  .social { display: flex; justify-content: center; gap: 80px; margin-top: 34px; }
  .social-dot { width: 48px; height: 48px; border-radius: 50%; background: var(--icon); }
  .contact-rule { width: 788px; height: 2px; background: #4a4f55; margin: 46px auto 0; }
  .join { margin-top: 30px; font-weight: 700; line-height: 56px; }
  .join-more { line-height: 56px; }
  .join-more a { color: var(--ink); text-decoration: underline; }

  .footer {
    height: 112px;
    background: var(--night);
    color: var(--footer-text);
    font-size: 30px;
    display: flex; align-items: center; justify-content: center;
  }
</style>
</head>
<body>
<main class="newsletter">
  <header class="masthead">
    <span class="brand-dot"></span>
    <span class="brand-name">VANTOR &amp; HALE</span>
  </header>

  <div class="hero" role="img" aria-label="Photo of a team around a wooden meeting table, hands taking notes"></div>

  <h2 class="section-title fees-title"><span>2021 NEW ERA - NEW FEES</span></h2>

  <section class="fee-grid">
    <div class="fee-card fee-card--exec">
      <p class="fee-label">TOP MANAGERS<br>EXECUTIVES</p>
      <p class="fee-rate">25%</p>
    </div>
    <div class="fee-card fee-card--other">
      <p class="fee-label">ALL OTHER<br>APPOINTMENTS</p>
      <p class="fee-rate">21%</p>
    </div>
  </section>

  <h2 class="section-title testimonials-title"><span>TESTIMONIALS</span></h2>

  <section class="testimonial">
    <div class="testimonial-photo" role="img" aria-label="Dimmed photo of a professional in a business meeting"></div>
    <div class="testimonial-copy">
      <p class="testimonial-kicker">What people say about us</p>
      <p class="testimonial-quote">Lorem ipsum dolor sit amet, consectetur adipiscing elit, sed do eiusmod tempor incididunt ut labore et dolore magna aliqua. Quis ipsum suspendisse ultrices gravida.</p>
      <p class="testimonial-author">- Mara Linde</p>
    </div>
  </section>

  <h2 class="section-title contact-title"><span>CONTACT&nbsp; INFORMATION</span></h2>

  <section class="contact">
    <p class="contact-address">4120 - 4136 Arden Lane,<br>Sampleton, KT4410 22RB<br>Telephone: +1 800 555 0147</p>
    <p class="contact-email">E-mail: hello@vantorhale.com</p>
    <div class="social" aria-label="Social channels">
      <span class="social-dot"></span>
      <span class="social-dot"></span>
      <span class="social-dot"></span>
      <span class="social-dot"></span>
    </div>
    <div class="contact-rule"></div>
    <p class="join">JOIN US in shaping the future of recruitment</p>
    <p class="join-more">For more information <a href="#">Click Here</a></p>
  </section>

  <footer class="footer">© 2020 | Privacy Policy</footer>
</main>
</body>
</html>
```